Qivera Health & Wellness Business Card Design

We would like to create business cards matching with our new logo design. The card should be professional looking but still have a playful side and something that would be eye catching. We are planing to open a luxury medical spa and looking to create a design based on this new logo. We are looking for a design that shows off luxury but not be gold in color. Also, while we are a more female oriented medical center we do have men that come in for our services and it should be be too feminine.

Target Market(s)

Health & Wellness. Medical patients. Luxury spa

Industry/Entity Type

Health And Wellness

Contact Information for Business Card

It should have the logo design in the front of card and back of card should have our contact information. Our current colors are peach/ coral, teal, and gray. We are looking for a modern looking design.

Font styles to use
Script

Colors
32a6d6
e667a6
86cfc6
fece3e

Requirements
Must have
• It should have our logo design. We would prefer to have a more modern look to the card.
Nice to have
• Eye-Catching Design on the personable side but still classy.
Should not have
• At this point we are looking for the best design. It should not have color purple.

```html
<!DOCTYPE html>
<html lang="en">
<head>
<meta charset="utf-8">
<title>Qivera Health &amp; Wellness Business Card</title>
<link rel="stylesheet" href="https://fonts.googleapis.com/css2?family=Open+Sans:wght@400;600&display=swap">
<style>
  :root {
    --bg: #3a3b3d;
    --brand-blue: #32a6d6;
    --paper: #e3e3e5;
    --ink: #1d1d1f;
    --rule: #a9a9ad;
    --logo-light: #eef2f5;
  }
  html, body {
    margin: 0;
    padding: 0;
    width: 1200px;
    height: 896px;
    overflow: hidden;
    background: var(--bg);
    font-family: "Open Sans", Arial, sans-serif;
  }
  .stage {
    position: relative;
    width: 1200px;
    height: 896px;
  }
  .card {
    position: absolute;
    top: 294px;
    width: 540px;
    height: 308px;
    box-sizing: border-box;
    overflow: hidden;
  }
  .card-front {
    left: 40px;
    background: var(--brand-blue);
    display: flex;
    align-items: center;
    justify-content: center;
  }
  .card-back {
    left: 620px;
    background: var(--paper);
    border-bottom: 12px solid var(--brand-blue);
  }
  .brand-name {
    font-weight: 400;
    font-size: 28px;
    letter-spacing: 0.5px;
    margin: 0;
  }
  .card-front .brand-name { color: var(--logo-light); }
  .card-back .brand-name {
    position: absolute;
    right: 28px;
    top: 118px;
    font-size: 22px;
    color: var(--ink);
  }
  .person {
    position: absolute;
    left: 34px;
    top: 42px;
  }
  .person-name {
    margin: 0;
    font-size: 20px;
    font-weight: 600;
    color: var(--brand-blue);
    letter-spacing: 0.8px;
    text-transform: uppercase;
  }
  .person-title {
    margin: 0 0 10px;
    font-size: 13px;
    color: var(--ink);
  }
  .contact-list {
    list-style: none;
    margin: 0;
    padding: 0;
    font-size: 13px;
    color: var(--ink);
    line-height: 20px;
  }
  .contact-list li {
    display: flex;
    align-items: center;
    gap: 7px;
  }
  .contact-icon { width: 12px; height: 12px; fill: var(--brand-blue); }
  .divider {
    position: absolute;
    left: 34px;
    right: 28px;
    top: 176px;
    height: 1px;
    background: var(--rule);
  }
  .address {
    position: absolute;
    right: 28px;
    top: 196px;
    margin: 0;
    font-style: normal;
    font-size: 14px;
    line-height: 19px;
    color: var(--ink);
    text-align: right;
  }
</style>
</head>
<body>
<main class="stage">
  <section class="card card-front" aria-label="Card front">
    <p class="brand-name">Qivera Health &amp; Wellness</p>
  </section>

  <section class="card card-back" aria-label="Card back">
    <div class="person">
      <p class="person-name">Marlen Okoye</p>
      <p class="person-title">Managing Director</p>
      <ul class="contact-list">
        <li>
          <svg class="contact-icon" viewBox="0 0 12 12" aria-hidden="true"><path d="M1 4c0-2 2-3 5-3s5 1 5 3l-2 1-1-2H4L3 5zM3 6h6l1 5H2z"/></svg>
          055-210 874 316
        </li>
        <li>
          <svg class="contact-icon" viewBox="0 0 12 12" aria-hidden="true"><path d="M3 0h6v12H3zM4 1v8h4V1z"/></svg>
          055-210 874 316
        </li>
        <li>
          <svg class="contact-icon" viewBox="0 0 12 12" aria-hidden="true"><path d="M0 2h12v8H0zM1 3l5 4 5-4z"/></svg>
          hello@qiveramail.com
        </li>
      </ul>
    </div>
    <p class="brand-name">Qivera Health &amp; Wellness</p>
    <div class="divider"></div>
    <address class="address">48 Linden Row, Suite 7<br>Harbor City, 204517</address>
  </section>
</main>
</body>
</html>
```